Unique Alcoholic Beverage (Beer Ice!) needs Exciting Package Design

We need a package designed for Tundro Beer Ice, an alcoholic flavored ice that is added to beer to keep it ice-cold and enhance the taste. Specifically we need graphics for shrink wrap designed to shrink 3 containers together, and graphics for a foil lid used to seal the containers that are shrink wrapped together.

The final design should communicate a fun and relaxed feel that fits with relaxed outdoor beer drinking, either at an outdoor event or simply relaxing outside with friends. See attachments and their descriptions below for more detail.

Attachments:
DESIGN REQUIREMENTS – this folder contains all of the specific design requirements, mostly contained within the word file.

DESIGN INSPIRATION – this folder contains examples of designs that appeal to us

LOGOS – this folder contains various examples of our current logo. We like our current logo but feel free to change it if you think it will make your overall design better. We are not locked in to the logo just yet.

PRODUCT EXAMPLES – this folder contains examples of the product itself to help you understand how it works and how it is packaged. In short, the product is packaged in what looks like a yogurt container with a foil lid. 3 “yogurt” containers are then stacked on top of each other and shrink wrapped together. You are designing the foil lid and the outer shrink wrap. Examples of the lid, the shrink wrap, and the product itself are in the “Product Examples” folder and described below:

Lid Example – a 3D rendering of the cup/lid combination. This in no way reflects what we are looking for design wise, it is only meant to help visualize the shape of the container. Note that the “cup” portion of this will be plain white, so we want the lid to really stand out and give the container some personality.

Shrink Examples (2) – this example is 4 wine glasses shrink wrapped together. We will be doing 3 “yogurt” cups instead of 4 wine glasses. Again, this is not meant to show what we are looking for graphic design wise, only to help you visualize the overall packaging shape.

Product Examples (2) - Including some pictures of the "beer ice" in use so you can get a sense of how the consumer will ultimately use the product. We want the consumer to immediately understand how to use it from the packaging.

Reason: Need additional time to review submissions. There will be no more extensions. Thanks!

Target Market(s)

Beer drinkers aged 25-45

Requirements
Must have
• - See design requirement folder attached. Note that the government requires all wording where we say "Must have". We would recommend using all the additional "recommended" wording we provide as well.
• Additional requirements:
• - Deliverable in Adobe Illustrator files
• - Designs for all 3 flavors (Lemon Shandy, Lime, Strawberry)
• - Designs for both the shrink wrap and the foil lids
Nice to have
• See design inspirations folder. We are looking for "simple with subtle details". We also want something that helps people "get it" immediately. Something that quickly conveys that this is ice meant to be put in a beer would be helpful.
Should not have
• No health benefit claims or anything targeted towards individuals under the age of 21.
• Seeing a lot of ice cubes incorporated into the designs. We want the packaging to project cold and refreshing, but ice cubes made of water suggest the product will water your beer down (it does not, since it is fruit flavored!). Would recommend avoiding water/ice cubes in the picture. Refreshing, fruity, and cold is what we want, just not watery. Thanks!

```html
<!DOCTYPE html>
<html lang="en">
<head>
<meta charset="utf-8">
<title>Tundro Beer Ice – Lemon Flavor Ice</title>
<link rel="stylesheet" href="https://fonts.googleapis.com/css2?family=Montserrat:wght@800&family=Oswald:wght@300;500&family=Pathway+Gothic+One&display=swap">
<style>
  :root {
    --ink: #231f20;
    --brand-blue: #4a86c8;
    --white: #ffffff;
    --orange: #f26c23;
    --green: #66bb46;
    --yellow: #f6c35a;
    --purple: #6c4c93;
  }
  html, body { margin: 0; padding: 0; overflow: hidden; background: var(--ink); }
  .label {
    position: relative;
    width: 1200px;
    height: 698px;
    overflow: hidden;
    background: var(--ink);
  }
  .paint-field { position: absolute; inset: 0; width: 1200px; height: 698px; }
  .product-title {
    position: absolute;
    top: 10px;
    left: 0;
    width: 1240px;
    margin: 0;
    text-align: center;
    font-family: "Montserrat", sans-serif;
    font-weight: 800;
    font-size: 128px;
    letter-spacing: 6px;
    line-height: 1;
    color: var(--brand-blue);
    -webkit-text-stroke: 12px var(--white);
    paint-order: stroke fill;
  }
  .brand-seal {
    position: absolute;
    left: 434px;
    top: 168px;
    width: 316px;
    height: 316px;
    box-sizing: border-box;
    border: 9px solid var(--white);
    border-radius: 50%;
    display: flex;
    align-items: center;
    justify-content: center;
  }
  .brand-name {
    font-family: "Oswald", sans-serif;
    font-weight: 500;
    font-size: 66px;
    letter-spacing: 10px;
    color: var(--white);
    margin-right: -10px;
  }
  .flavor-name {
    position: absolute;
    top: 540px;
    left: 0;
    width: 1200px;
    margin: 0;
    text-align: center;
    font-family: "Oswald", sans-serif;
    font-weight: 300;
    font-size: 44px;
    letter-spacing: 1px;
    color: var(--brand-blue);
    text-indent: 0;
    padding-left: 0;
  }
  .usage-steps {
    position: absolute;
    left: 885px;
    top: 288px;
    width: 400px;
    height: 184px;
    transform: rotate(-90deg);
    margin: 0;
    padding: 0 0 0 14px;
    box-sizing: border-box;
    font-family: "Pathway Gothic One", sans-serif;
    font-size: 13.4px;
    line-height: 15.5px;
    color: var(--ink);
    list-style: disc;
  }
  .usage-steps li { margin-bottom: 5px; }
</style>
</head>
<body>
<main class="label">
  <svg class="paint-field" viewBox="0 0 1200 698" aria-hidden="false">
    <defs>
      <linearGradient id="left-paint" x1="0" y1="0" x2="0.6" y2="1">
        <stop offset="0" stop-color="var(--orange)"/>
        <stop offset="0.45" stop-color="var(--orange)"/>
        <stop offset="0.75" stop-color="var(--green)"/>
        <stop offset="1" stop-color="var(--green)"/>
      </linearGradient>
      <linearGradient id="right-paint" x1="0.5" y1="0" x2="0.2" y2="1">
        <stop offset="0" stop-color="var(--yellow)"/>
        <stop offset="0.4" stop-color="var(--yellow)"/>
        <stop offset="0.5" stop-color="var(--purple)"/>
        <stop offset="1" stop-color="var(--purple)"/>
      </linearGradient>
    </defs>
    <path role="img" aria-label="Orange and green brush-stroke paint swathes"
          fill="url(#left-paint)"
          d="M0,0 L330,0 C350,120 260,230 300,330 C390,440 395,600 345,698 L0,698 Z"/>
    <path role="img" aria-label="Yellow and purple brush-stroke paint swathes"
          fill="url(#right-paint)"
          d="M905,0 L1200,0 L1200,698 L860,698 C790,600 800,400 875,300 C925,210 880,110 905,0 Z"/>
  </svg>

  <h1 class="product-title">BEER ICE</h1>

  <div class="brand-seal">
    <span class="brand-name">TUNDRO</span>
  </div>

  <p class="flavor-name">LEMON FLAVOR ICE</p>

  <ul class="usage-steps">
    <li>Freeze in your freezer overnight. If you're in a rush a few hours will do the trick if you don't mind the ice melting faster (also flavors your beer faster).</li>
    <li>Drop Tundro into your favorite beer. Or get creative and try them in all kinds of beverages! We recommend putting the ice in the glass first, but if you're really talented try putting it in last (tip: submerge the rim of the cup before squeezing the ice out).</li>
    <li>Enjoy the flavor experience of Tundro. As the ice melts the flavor of your beverage slowly changes for a truly unique and ice cold experience!</li>
  </ul>
</main>
</body>
</html>
```